I have an animal hospital. I want a poster to hang in each exam room to show a picture of a normal sized heart and then an enlarged heart of a dog that was fed a grain-free diet. I want to warn people not to feed grain-free diets. Maybe at the top of the poster, "Do you feed grain-free?" and then the x-ray comparison, then the warnings of Canine Dilated Cardiomyopathy.

```html
<!DOCTYPE html>
<html lang="en">
<head>
<meta charset="utf-8">
<title>Do You Feed Grain-Free? – Exam Room Poster</title>
<link href="https://fonts.googleapis.com/css2?family=Montserrat:wght@400;500;700;800&display=swap" rel="stylesheet">
<style>
  :root{
    --orange:#d4622a;
    --charcoal:#4a4a4a;
    --frame:#5a5a5a;
    --paper:#f4f4f3;
    --backdrop:#9c9c9c;
    --warning:#e8a915;
    --xray-dark:#141414;
    --xray-light:#b9b9b9;
    --dog:#a8643a;
  }
  *{box-sizing:border-box;margin:0;padding:0}
  html,body{width:1200px;height:674px;overflow:hidden}
  body{background:var(--backdrop);font-family:'Montserrat',sans-serif;position:relative}

  .poster{position:absolute;left:350px;top:17px;width:500px;height:640px;background:var(--paper);overflow:hidden;box-shadow:0 4px 14px rgba(0,0,0,.25)}

  .corner-blob{position:absolute;right:0;top:0;width:150px;height:160px}

  .headline{position:absolute;left:30px;top:30px;color:var(--charcoal);font-weight:800;line-height:.95;text-transform:uppercase}
  .headline .lead{font-size:29px;letter-spacing:1px}
  .headline .feed{font-size:70px;color:var(--orange);letter-spacing:1px;line-height:.9}
  .headline .grain{font-size:27px;letter-spacing:1px}

  .big-question{position:absolute;left:282px;top:-10px;font-size:140px;font-weight:800;color:var(--charcoal);font-family:Georgia,'Times New Roman',serif;line-height:1}

  .xray-panel{position:absolute;border:7px solid var(--frame);background:var(--frame)}
  .xray-panel .film{width:100%;height:100%;background:radial-gradient(ellipse 45% 50% at 50% 58%,var(--xray-light),#555 60%,var(--xray-dark) 100%)}
  .xray-panel .label{position:absolute;top:-7px;background:var(--orange);color:#fff;font-weight:700;text-transform:uppercase;letter-spacing:1px;padding:4px 10px;white-space:nowrap}
  .xray-panel.normal{left:28px;top:192px;width:205px;height:178px}
  .xray-panel.normal .label{right:-7px;font-size:11px}
  .xray-panel.enlarged{left:250px;top:150px;width:225px;height:205px}
  .xray-panel.enlarged .label{left:-7px;right:-7px;font-size:14px;padding:5px 10px}
  .warning-icon{position:absolute;left:236px;top:300px;width:76px;height:58px}

  .symptoms{position:absolute;left:30px;top:380px;width:440px;font-size:9px;color:var(--charcoal);line-height:12px}
  .intro{font-weight:500;width:300px;margin-bottom:3px}
  .check-columns{display:flex;gap:30px;width:300px;margin-bottom:6px}
  .check-list{list-style:none}
  .check-list li{color:var(--orange);font-weight:700;font-size:10.5px;padding-left:16px;position:relative;line-height:14px}
  .check-list li svg{position:absolute;left:0;top:3px;width:11px;height:9px}
  .note{width:300px;margin-bottom:4px}
  .signs{margin-top:6px}
  .signs li{font-size:10px;line-height:12.5px;margin-bottom:3px}
  .signs li svg{top:2px}

  .dog-blob{position:absolute;right:0;top:330px;width:190px;height:190px}
  .dog-photo{position:absolute;right:15px;top:360px;width:140px;height:150px;border-radius:65px 65px 18px 18px;background:linear-gradient(160deg,#c07a48,var(--dog) 55%,#7e4424)}
</style>
</head>
<body>
  <main class="poster">
    <svg class="corner-blob" viewBox="0 0 150 160" aria-hidden="true">
      <path d="M0 0 H150 V160 C120 150 110 110 90 95 C70 80 40 85 35 60 C30 35 10 25 0 0Z" fill="var(--orange)"/>
      <path d="M20 55 C50 70 80 55 110 70 C130 80 140 110 150 120" fill="none" stroke="#fff" stroke-width="1.5"/>
      <path d="M25 62 C55 78 85 62 112 78 C128 88 138 115 150 128" fill="none" stroke="#fff" stroke-width="1"/>
    </svg>

    <h1 class="headline">
      <span class="lead">Do you</span><br>
      <span class="feed">Feed</span><br>
      <span class="grain">Grain-free?</span>
    </h1>
    <div class="big-question" aria-hidden="true">?</div>

    <figure class="xray-panel normal">
      <div class="film" role="img" aria-label="Chest x-ray of a dog with a normal sized heart"></div>
      <figcaption class="label">Normal heart</figcaption>
    </figure>
    <figure class="xray-panel enlarged">
      <div class="film" role="img" aria-label="Chest x-ray of a dog with an enlarged heart"></div>
      <figcaption class="label">Enlarged heart</figcaption>
    </figure>
    <svg class="warning-icon" viewBox="0 0 80 62" aria-hidden="true">
      <path d="M40 5 L76 57 H4 Z" fill="none" stroke="var(--warning)" stroke-width="5" stroke-linejoin="round"/>
      <rect x="37" y="22" width="6" height="20" rx="2" fill="var(--warning)"/>
      <circle cx="40" cy="49" r="3.5" fill="var(--warning)"/>
    </svg>

    <svg class="dog-blob" viewBox="0 0 190 190" preserveAspectRatio="none" aria-hidden="true">
      <path d="M190 10 C160 0 125 25 115 60 C105 95 60 90 45 125 C30 160 55 180 40 190 H190 Z" fill="var(--orange)"/>
    </svg>
    <div class="dog-photo" role="img" aria-label="Photo of a red-brown short-haired dog tilting its head"></div>

    <section class="symptoms">
      <p class="intro">The major symptoms of DCM include:</p>
      <div class="check-columns">
        <ul class="check-list">
          <li><svg viewBox="0 0 11 9"><path d="M1 5 L4 8 L10 1" fill="none" stroke="var(--orange)" stroke-width="2"/></svg>Lethargy</li>
          <li><svg viewBox="0 0 11 9"><path d="M1 5 L4 8 L10 1" fill="none" stroke="var(--orange)" stroke-width="2"/></svg>Anorexia</li>
          <li><svg viewBox="0 0 11 9"><path d="M1 5 L4 8 L10 1" fill="none" stroke="var(--orange)" stroke-width="2"/></svg>Labored breathing</li>
          <li><svg viewBox="0 0 11 9"><path d="M1 5 L4 8 L10 1" fill="none" stroke="var(--orange)" stroke-width="2"/></svg>Panting</li>
        </ul>
        <ul class="check-list">
          <li><svg viewBox="0 0 11 9"><path d="M1 5 L4 8 L10 1" fill="none" stroke="var(--orange)" stroke-width="2"/></svg>Coughing</li>
          <li><svg viewBox="0 0 11 9"><path d="M1 5 L4 8 L10 1" fill="none" stroke="var(--orange)" stroke-width="2"/></svg>Abdominal distension</li>
          <li><svg viewBox="0 0 11 9"><path d="M1 5 L4 8 L10 1" fill="none" stroke="var(--orange)" stroke-width="2"/></svg>Sudden collapse</li>
        </ul>
      </div>
      <p class="note">In some cases, dogs with preclinical DCM (prior to the appearance of symptoms) may be given a questionable diagnosis if they appear to be in fine health.</p>
      <p class="note">On the other hand, a thorough physical exam can reveal some of the subtle symptoms of DCM, such as:</p>
      <ul class="check-list signs">
        <li><svg viewBox="0 0 11 9"><path d="M1 5 L4 8 L10 1" fill="none" stroke="var(--orange)" stroke-width="2"/></svg>Pulse deficits</li>
        <li><svg viewBox="0 0 11 9"><path d="M1 5 L4 8 L10 1" fill="none" stroke="var(--orange)" stroke-width="2"/></svg>Premature heart contractions that originate in or above the ventricles</li>
        <li><svg viewBox="0 0 11 9"><path d="M1 5 L4 8 L10 1" fill="none" stroke="var(--orange)" stroke-width="2"/></svg>Slow capillary refill time in the mucous membrane tissues (e.g., gums are slow to turn pink again after pressing on them gently), indicating poor circulation</li>
        <li><svg viewBox="0 0 11 9"><path d="M1 5 L4 8 L10 1" fill="none" stroke="var(--orange)" stroke-width="2"/></svg>Breathing sounds muffled or crackly due to the presence of fluid in the lungs</li>
      </ul>
    </section>
  </main>
</body>
</html>
```